Webdesign Hauskranken- und Tagespflege „Am Lindenhof“
Zielgruppe
Die Hauskranken- und Tagespflege „Am Lindenhof“ in Chemnitz ist ein unabhängiges, privat geführtes Unternehmen im Bereich der ambulanten und teilstationären Kranken- und Seniorenpflege. Seit der Gründung am 1. Mai 2007 stehen wir für eine zuverlässige, individuelle und herzliche Betreuung unserer Klientinnen und Klienten.
Das Team ist ein engagiertes Pflegeteam und auf über 35 qualifizierte Mitarbeiterinnen und Mitarbeiter angewachsen. Gemeinsam setzen wir uns täglich dafür ein, Menschen mit Pflegebedarf eine bestmögliche Versorgung und ein hohes Maß an Lebensqualität zu ermöglichen.
Unsere Firmenphilosophie basiert auf Wertschätzung, Vertrauen und Respekt – sowohl im Umgang mit unseren Klientinnen und Klienten sowie deren Angehörigen als auch innerhalb unseres Teams. Eine persönliche, einfühlsame und fachlich kompetente Betreuung steht für uns an erster Stelle.
Ob Grundpflege oder Behandlungspflege – bei uns sind Sie in guten Händen. Wir begleiten unsere Klientinnen und Klienten mit Fürsorge, Fachkompetenz und Herz und unterstützen sie dabei, ihren Alltag so selbstbestimmt wie möglich zu gestalten.
Gleichzeitig entlasten wir Angehörige, Freunde und Bekannte, indem wir ihnen Sicherheit geben und Freiräume schaffen. So bleibt mehr Zeit für gemeinsame, unbeschwerte Momente mit den Menschen, die ihnen am Herzen liegen.
Unsere Tagespflege bietet Platz für 18 Gäste. Der große Aufenthaltsraum mit offener Küche lädt zum gemütlichen Beisammensein ein. In unserem Ruheraum können sich unsere Gäste bei Bedarf zurückziehen und sich ausruhen, auch Therapien (Logopädie, Ergotherapie, Physiotherapie…) werden darin durchgeführt. Der Aufenthaltsraum ist zum Teil eingerichtet wie eine gemütliche Wohnstube, ihre Einrichtung erinnert an frühere Zeiten. Gemütliche Ruhesessel laden zum Entspannen ein.
Der persönliche Kontakt und das Vertrauen unserer Patientinnen und Patienten bilden dabei st..
Aufgabenstellung
Ziele des Relaunchs:
modernes, freundliches und barrierearmes Design
klare Benutzerführung für Senioren und Angehörige
Hinweis zum Rückrufservice
Notfallnummer dauerhaft sichtbar
schnelle Kontaktaufnahme (Telefon, Rückruf, Kontaktformular)
bessere Auffindbarkeit bei Google (SEO)
Vertrauen durch authentische Bilder, Teamvorstellung und Bewertungen

```html
<!DOCTYPE html>
<html lang="de">
<head>
<meta charset="utf-8">
<title>Hauskranken- und Tagespflege „Am Lindenhof“</title>
<link href="https://fonts.googleapis.com/css2?family=Poppins:wght@300;400;500;600;700&display=swap" rel="stylesheet">
<style>
:root{
  --navy:#2e3b82;
  --navy-dark:#25306b;
  --slate:#3b4650;
  --sky:#1e9fe0;
  --yellow:#ffe61a;
  --ice:#e4f0fb;
  --text:#333840;
  --muted:#8a8f96;
  --white:#ffffff;
  --star:#f5b400;
}
*{box-sizing:border-box;margin:0;padding:0}
html,body{width:1200px;height:3224px;overflow:hidden}
body{position:relative;background:var(--white);font-family:"Poppins",sans-serif;color:var(--text)}
.abs{position:absolute}
.btn{position:absolute;display:flex;align-items:center;justify-content:center;background:var(--navy);color:var(--white);font-size:12.5px;font-weight:600;border-radius:3px;white-space:nowrap}

/* top bar */
.topbar-hours{left:438px;top:26px;font-size:13.5px;color:#444;display:flex;align-items:center;gap:8px;white-space:nowrap}
.hotline{left:954px;top:8px;width:164px;height:43px;background:var(--yellow);border-radius:3px;display:flex;align-items:center;gap:8px;padding-left:10px}
.hotline small{display:block;font-size:10px;color:#6a5d00;line-height:1}
.hotline strong{display:block;font-size:15px;font-weight:600;color:#222;line-height:1.3}
.nav{left:0;top:57px;width:1200px;height:75px;background:var(--slate)}
.nav-home{left:311px;top:57px;width:61px;height:75px;background:var(--sky);display:flex;align-items:center;justify-content:center}
.nav-links{left:400px;top:57px;height:75px;display:flex;align-items:center;gap:25px;color:var(--white);font-size:14px;white-space:nowrap}
.brand{left:128px;top:28px;width:112px;height:112px;border-radius:50%;background:var(--yellow);display:flex;align-items:center;justify-content:center;text-align:center;font-size:14px;font-weight:600;color:var(--navy-dark);line-height:1.2;z-index:3}

/* hero */
.hero{left:71px;top:132px;width:1057px;height:413px;border-radius:0 0 28px 28px;background:linear-gradient(100deg,#6fb7a2 0%,#9ccbb8 25%,#e9e6df 45%,#f2efe9 62%,#cfd8c7 82%,#a9c09c 100%)}
.hero-card{left:826px;top:230px;width:261px;height:180px;background:var(--white);padding:26px 20px}
.hero-card h2{font-size:19px;font-weight:600;color:var(--navy);line-height:23px;letter-spacing:-.1px;white-space:nowrap}

/* intro */
.section-title{position:absolute;left:0;width:1200px;text-align:center;font-size:28px;font-weight:600;color:#2d2f33}
.intro-text{left:140px;top:643px;width:920px;text-align:center;font-size:12.3px;line-height:19px;color:#444}

.service{width:452px;height:283px;top:725px;background:var(--white);box-shadow:0 1px 4px rgba(0,0,0,.18)}
.service .photo{position:absolute;left:0;top:0;width:100%;height:232px}
.service .badge{position:absolute;left:23px;top:195px;width:112px;height:112px;border-radius:50%;background:var(--yellow);display:flex;align-items:center;justify-content:center}
.service .label{position:absolute;left:144px;top:244px;font-size:19.5px;font-weight:600;color:#2d2f33;letter-spacing:.3px}
.service .chev{position:absolute;right:38px;top:246px}

/* Leitbild */
.leitbild{left:139px;top:1068px;width:923px;height:375px;background:var(--ice);border-radius:60px 0 60px 0}
.round-photo{border-radius:50%}
.block-title{font-size:28px;font-weight:600;color:#2d2f33;white-space:nowrap}
.block-text{font-size:12px;line-height:15px;color:#444}

/* reviews */
.review{top:1953px;width:292px;height:262px;background:var(--white);box-shadow:0 2px 10px rgba(0,0,0,.08);padding:44px 21px 0}
.review p{font-size:14px;line-height:25.5px;color:#333;margin-top:10px}
.review .who{font-size:13.5px;color:var(--muted);margin-top:26px}
.stars{display:flex;gap:2px;margin-top:10px}
.dots{left:580px;top:2249px;display:flex;gap:8px}
.dots span{width:5px;height:5px;border-radius:50%;background:#555}
.dots span.off{background:#bbb}

/* contact */
.map{left:138px;top:2358px;width:924px;height:300px;background:linear-gradient(135deg,#eef0f2 0%,#e6ebe4 50%,#d6ecd9 100%)}
.map-card{left:140px;top:2360px;width:226px;height:108px;background:var(--white);box-shadow:0 1px 3px rgba(0,0,0,.2);padding:12px 12px}
.map-card strong{display:block;font-size:10.5px;font-weight:500;line-height:15px;color:#222;width:140px}
.map-card span{display:block;font-size:8.5px;line-height:12px;color:#666}
.contact-bar{left:138px;top:2658px;width:924px;height:117px;background:var(--white);box-shadow:0 1px 4px rgba(0,0,0,.15)}
.contact-item{position:absolute;top:2698px;display:flex;gap:18px;align-items:flex-start}
.contact-item .ico{width:44px;height:44px;border-radius:50%;background:var(--sky);display:flex;align-items:center;justify-content:center;flex-shrink:0}
.contact-item h4{font-size:13.5px;font-weight:600;color:#222;margin-bottom:6px}
.contact-item p{font-size:12.3px;line-height:14px;color:#333}

/* cta band */
.cta{left:0;top:2826px;width:1200px;height:202px;background:linear-gradient(90deg,#eaf3fb 0%,#e6f0f9 45%,#f1ebe4 65%,#dfd4c8 100%)}
.cta-text{left:162px;top:2895px;font-size:17.5px;line-height:21px;color:var(--navy)}
.cta-text strong{font-weight:600}

/* footer */
.footer{left:0;top:3028px;width:1200px;height:196px;background:var(--navy)}
.footer-brand{left:146px;top:3058px;width:104px;height:104px;border-radius:50%;background:var(--yellow);display:flex;align-items:center;justify-content:center;text-align:center;font-size:13px;font-weight:600;color:var(--navy-dark);line-height:1.2}
.footer-nav{left:336px;top:3090px;display:flex;gap:26px;color:var(--white);font-size:14px;white-space:nowrap}
.footer-line{left:336px;top:3160px;width:726px;height:1px;background:rgba(255,255,255,.35)}
.footer-legal{left:336px;top:3182px;font-size:12px;color:#c9cfe6}
.footer-copy{right:138px;top:3182px;font-size:12px;color:#c9cfe6}
</style>
</head>
<body>

<div class="abs topbar-hours">
  <svg width="15" height="15" viewBox="0 0 16 16" fill="none" stroke="#444" stroke-width="1.4"><circle cx="8" cy="8" r="6.5"/><path d="M8 4.5V8l2.5 1.5"/></svg>
  <span><strong>Mo - Do:</strong> 9:00 – 15:00 Uhr | <strong>Fr:</strong> 9:00 – 14:00 Uhr | und nach Vereinbarung</span>
</div>
<div class="abs hotline">
  <svg width="26" height="26" viewBox="0 0 26 26" fill="#fff" stroke="#333" stroke-width="1.3"><circle cx="13" cy="13" r="12"/><path d="M8 15v-3a5 5 0 0 1 10 0v3M7 13h2v4H7zM17 13h2v4h-2zM18 17c0 2-2 3-4 3" fill="none"/></svg>
  <div><small>24h-Hotline</small><strong>0371 / 4417230</strong></div>
</div>

<nav>
  <div class="abs nav"></div>
  <div class="abs nav-home">
    <svg width="16" height="15" viewBox="0 0 16 15" fill="#fff"><path d="M8 1 1 7.5h2V14h4v-4h2v4h4V7.5h2z"/></svg>
  </div>
  <div class="abs nav-links">
    <span>Über uns</span><span>Team</span><span>Pflegeleitbild</span><span>Partner</span><span>Hauskrankenpflege</span><span>Tagespflege</span><span>Aktuelles</span>
  </div>
</nav>
<div class="abs brand">Am<br>Lindenhof</div>

<div class="abs hero" role="img" aria-label="Foto: Pflegerin im Gespräch mit einer lächelnden Seniorin"></div>
<div class="abs hero-card">
  <h2>Helft denen, die Hilfe<br>brauchen. Mitarbeiter<br>gesucht!!!</h2>
  <div class="btn" style="left:21px;top:116px;width:150px;height:40px">Mehr dazu erfahren</div>
</div>

<h1 class="section-title" style="top:600px">Ihr Pflegeteam aus Chemnitz</h1>
<p class="abs intro-text">Die Hauskranken- und Tagespflege „Am Lindenhof“ in Chemnitz ist ein unabhängiges, privat geführtes Unternehmen im Bereich der ambulanten und teilstationären Kranken- und Seniorenpflege. Seit der Gründung am 1. Mai 2007 stehen wir für eine zuverlässige, individuelle und herzliche Betreuung unserer Klientinnen und Klienten.</p>

<div class="abs service" style="left:138px">
  <div class="photo" role="img" aria-label="Foto: Blutdruckmessung bei einer Patientin" style="background:linear-gradient(120deg,#7fc9de 0%,#4fb3cf 40%,#2f4b6b 70%,#9fd3e3 100%)"></div>
  <div class="badge">
    <svg width="52" height="56" viewBox="0 0 52 56" fill="none" stroke="#333" stroke-width="2.2" stroke-linecap="round"><path d="M10 4H6v16a10 10 0 0 0 20 0V4h-4"/><path d="M16 30v10a10 10 0 0 0 20 0v-6"/><circle cx="36" cy="29" r="5"/><circle cx="36" cy="29" r="1.5"/></svg>
  </div>
  <span class="label">HAUSKRANKENPFLEGE</span>
  <svg class="chev" width="12" height="18" viewBox="0 0 12 18" fill="none" stroke="#333" stroke-width="2.2"><path d="M2 2l7 7-7 7"/></svg>
</div>
<div class="abs service" style="left:609px">
  <div class="photo" role="img" aria-label="Foto: Seniorinnen und Betreuerin in der Tagespflege" style="background:linear-gradient(110deg,#9aa39b 0%,#d9d7d2 35%,#c9a88f 60%,#e5e2de 100%)"></div>
  <div class="badge">
    <svg width="56" height="56" viewBox="0 0 56 56" fill="none" stroke="#333" stroke-width="2.2" stroke-linejoin="round"><path d="M6 26 28 6l22 20M12 21v29h32V21"/><path d="M28 44s-11-7-11-14a5.5 5.5 0 0 1 11-2 5.5 5.5 0 0 1 11 2c0 7-11 14-11 14z"/><path d="M28 30v8M24 34h8"/></svg>
  </div>
  <span class="label">TAGESPFLEGE</span>
  <svg class="chev" width="12" height="18" viewBox="0 0 12 18" fill="none" stroke="#333" stroke-width="2.2"><path d="M2 2l7 7-7 7"/></svg>
</div>

<section>
  <div class="abs leitbild"></div>
  <div class="abs round-photo" role="img" aria-label="Foto: Pflegerin und Seniorin lächelnd nebeneinander" style="left:170px;top:1085px;width:336px;height:336px;background:linear-gradient(120deg,#f3efe9 0%,#e8d9c6 40%,#c9b8a8 70%,#8e8a87 100%)"></div>
  <h2 class="abs block-title" style="left:587px;top:1148px">Unser Pflegeleitbild</h2>
  <p class="abs block-text" style="left:588px;top:1197px;width:436px">Jeder Mensch hat den Wunsch mit Respekt und liebevoller Zuwendung versorgt zu werden. Das Ziel unserer Einrichtung ist unsere Betreuten bzw. ihre Angehörigen bei der Pflege und Bewältigung des Alltags im häuslichen Umfeld, in dieser Weise zu unterstützen. Somit kann eine Lebensführung und eine aktive Teilnahme an der Gesellschaft ermöglicht werden.</p>
  <div class="btn" style="left:589px;top:1310px;width:150px;height:41px">Mehr dazu erfahren</div>
</section>

<section>
  <h2 class="abs block-title" style="left:189px;top:1527px">Unser Pflegeteam</h2>
  <div class="abs block-text" style="left:191px;top:1575px;width:446px">
    <p>Das Team ist ein engagiertes Pflegeteam und auf über 35 qualifizierte Mitarbeiterinnen und Mitarbeiter angewachsen. Gemeinsam setzen wir uns täglich dafür ein, Menschen mit Pflegebedarf eine bestmögliche Versorgung und ein hohes Maß an Lebensqualität zu ermöglichen.</p>
    <p style="margin-top:15px">Unsere Firmenphilosophie basiert auf Wertschätzung, Vertrauen und Respekt – sowohl im Umgang mit unseren Klientinnen und Klienten sowie deren Angehörigen als auch innerhalb unseres Teams. Eine persönliche, einfühlsame und fachlich kompetente Betreuung steht für uns an erster Stelle.</p>
  </div>
  <div class="btn" style="left:190px;top:1743px;width:150px;height:41px">Mehr dazu erfahren</div>
  <div class="abs round-photo" role="img" aria-label="Foto: Pflegerin kümmert sich um eine Seniorin im Rollstuhl" style="left:678px;top:1496px;width:340px;height:340px;background:linear-gradient(120deg,#eef0ef 0%,#7fc7bd 35%,#c58b64 55%,#f3f1ee 80%,#d7d4cf 100%)"></div>
</section>

<h2 class="section-title" style="top:1893px">Bewertungen</h2>
<div class="abs review" style="left:139px">
  <svg width="34" height="26" viewBox="0 0 34 26" fill="none" stroke="#999" stroke-width="1.5"><path d="M2 2h12v12l-6 10H4l5-10H2zM19 2h12v12l-6 10h-4l5-10h-7z"/></svg>
  <div class="stars"><svg width="86" height="16" viewBox="0 0 86 16" fill="var(--star)"><g id="st"><path d="M8 1l2.1 4.5 4.9.6-3.6 3.4.9 4.9L8 12l-4.3 2.4.9-4.9L1 6.1l4.9-.6z"/></g><use href="#st" x="17"/><use href="#st" x="34"/><use href="#st" x="51"/><use href="#st" x="68"/></svg></div>
  <p>The quality is better than anything I've used — and the prices are unbelievable."</p>
  <div class="who">- Verified Customer</div>
</div>
<div class="abs review" style="left:452px">
  <svg width="34" height="26" viewBox="0 0 34 26" fill="none" stroke="#999" stroke-width="1.5"><path d="M2 2h12v12l-6 10H4l5-10H2zM19 2h12v12l-6 10h-4l5-10h-7z"/></svg>
  <div class="stars"><svg width="86" height="16" viewBox="0 0 86 16" fill="var(--star)"><use href="#st"/><use href="#st" x="17"/><use href="#st" x="34"/><use href="#st" x="51"/><use href="#st" x="68"/></svg></div>
  <p>The quality is better than anything I've used — and the prices are unbelievable."</p>
  <div class="who">- Verified Customer</div>
</div>
<div class="abs review" style="left:769px">
  <svg width="34" height="26" viewBox="0 0 34 26" fill="none" stroke="#999" stroke-width="1.5"><path d="M2 2h12v12l-6 10H4l5-10H2zM19 2h12v12l-6 10h-4l5-10h-7z"/></svg>
  <div class="stars"><svg width="86" height="16" viewBox="0 0 86 16" fill="var(--star)"><use href="#st"/><use href="#st" x="17"/><use href="#st" x="34"/><use href="#st" x="51"/><use href="#st" x="68"/></svg></div>
  <p>The quality is better than anything I've used — and the prices are unbelievable."</p>
  <div class="who">- Verified Customer</div>
</div>
<div class="abs dots"><span></span><span class="off"></span><span></span><span></span></div>

<h2 class="section-title" style="top:2304px">Kontakt</h2>
<div class="abs map" role="img" aria-label="Karte: Standort der Hauskranken- und Tagespflege in Chemnitz"></div>
<div class="abs map-card">
  <strong>Hauskranken- und Tagespflege am Lindenhof GmbH</strong>
  <span>Lindenstraße 24, 09130</span>
  <span>Chemnitz-Lindenviertel, Germany</span>
</div>
<div class="abs contact-bar"></div>
<div class="contact-item" style="left:198px">
  <div class="ico"><svg width="24" height="24" viewBox="0 0 24 24" fill="none" stroke="#fff" stroke-width="1.6"><path d="M5 14v-3a7 7 0 0 1 14 0v3M4 12h3v5H4zM17 12h3v5h-3zM18.5 17c0 2.5-2.5 3.5-5 3.5"/></svg></div>
  <div><h4>Rufen Sie uns an</h4><p>24h-Hotline<br>0371 / 4417230</p></div>
</div>
<div class="contact-item" style="left:488px">
  <div class="ico"><svg width="22" height="24" viewBox="0 0 22 24" fill="none" stroke="#fff" stroke-width="1.6"><path d="M11 22s7-7 7-13a7 7 0 0 0-14 0c0 6 7 13 7 13z"/><circle cx="11" cy="9" r="2.5"/></svg></div>
  <div><h4>Ort</h4><p>Lindenstraße 24<br>09130 Chemnitz</p></div>
</div>
<div class="contact-item" style="left:776px">
  <div class="ico"><svg width="24" height="24" viewBox="0 0 24 24" fill="none" stroke="#fff" stroke-width="1.6"><circle cx="12" cy="12" r="8.5"/><path d="M12 7v5l3 2"/></svg></div>
  <div><h4>Öffnungszeiten</h4><p>Mo - Do: 9:00 - 15:00 Uhr<br>Fr: 9:00 - 14:00 Uhr<br>und nach Vereinbarung</p></div>
</div>

<div class="abs cta" role="img" aria-label="Foto: Hände, die eine ältere Hand halten"></div>
<p class="abs cta-text"><strong>Der persönliche Kontakt und das Vertrauen</strong><br>unserer Patientinnen und Patienten bilden dabei<br>stets den Mittelpunkt unseres Handelns.</p>

<footer>
  <div class="abs footer"></div>
  <div class="abs footer-brand">Am<br>Lindenhof</div>
  <div class="abs footer-nav"><span>Home</span><span>Über uns</span><span>Team</span><span>Pflegeleitbild</span><span>Partner</span><span>Hauskrankenpflege</span><span>Tagespflege</span><span>Aktuelles</span></div>
  <div class="abs footer-line"></div>
  <div class="abs footer-legal">Impressum &nbsp;|&nbsp; Datenschutz &nbsp;|&nbsp; Erklärung zur Barrierefreiheit</div>
  <div class="abs footer-copy">© 2026 Am Lindenhof</div>
</footer>

</body>
</html>
```